Label Wanted For New, Millennial, Hard Apple Cider Brand

California, alcoholic apple cider brand targeted towards Millennials needs a label to show product as:

Hand-crafted. Modern. Hipster. Produced from apples. Delicious. Unisex.

We are primarily a small wine producer (500cs/year - 20 barrels/year). Check the attachments for one of our current labels. Tidewhistle will be the name of our cider.

This is the first release of our cider. This cider bottle we will be using is attached (Champagne Mold with a Crown Cap).

We will have several flavors over the course of the next few years and need a placeholder on the front label for the specific style:
"Off-Dry" (Tart + a Little Sweet)
"Dry" (Crisp + Tart)
"Hopped" (Fermented with Hopps)
"HoneyBee" (Fermented with Honey)
"Barrel Aged" (Aged in Barrel)
"Cross Culture" (Fermented with Wine Yeast and Viognier), etc.

Looking for a label that is modern, but also somewhat rustic. Please view our "Labels We Like" file. Something creative and different. Definitely more on the hipster side of things than old-fashioned.
Updates

Project Deadline Extended Reason: Hi designers,We are postponing the deadline due to the holidays. We've been unable to provide effective feedback to many of you with the craziness of Christmas Eve, Christmas and now New Years! Thank you for your patience. We will have feedback for many of you tomorrow and final selections on January 02. Thank you for all of your hard work. - Noor Added Friday, December 26, 2014

Target Market(s)

26-44yr old, educated, outdoorsy, food/wine loving, beer/wine/spirit drinking adults. Unisex product - should be slightly more masculine than feminine.

Industry/Entity Type

Product

Font styles to use
Decorative

Requirements
Must have
• Front:
• 1. Front Label Measurements: Maintain a 4(w) x 4.125(h) inch front with 1/4in bleed.
• 2. Font used for brand name "Tidewhistle" should be legible but unique.
• 3. Artwork should be unisex. Modern with a handcrafted look.
• 4. Front Label Must Contain the Following Info:
• a. "Alc / Vol 7.0%"
• b. California Hard Apple Cider
• c. Placeholder for style of cider (DRY, HOPPED, OFF-DRY, etc.)
• Back Label:
• 1. Back Label Measurements: Maintain a 3(w) x 4.125(h) inch back w/ 1/4in bleed. One back label will be used for all ciders
• 2. Back Label Must Contain the Following Info:
• a. "GOVERNMENT WARNING: (1) ACCORDING TO THE SURGEON GENERAL, WOMEN SHOULD NOT DRINK ALCOHOLIC BEVERAGES DURING PREGNANCY BECAUSE OF THE RISK OF BIRTH DEFECTS. (2) CONSUMPTION OF ALCOHOLIC BEVERAGES IMPAIRS YOUR ABILITY TO DRIVE A CAR OR OPERATE MACHINERY, AND MAY CAUSE HEALTH PROBLEMS."
• b. "CONTAINS SULFITES"
• c. "Produced & Bottled by FM Vine Co, Buellton, CA".
• d. Back label copy. T
• "We Love-love cider. Call us crazy, but we feel that cider just might be the bridge between beer-only drinkers and wine-only drinkers - a white flag of sorts. Go on, shake hands. Finally something we can all agree on. Break free from the norm. Drink what you love. Cheers. Noor K."
Nice to have
• 1. OPEN THE "LABELS I LIKE" FILE. Do not submit a design before looking a this file.
• 2. Label must tie in brand name, "Tide Whistle" with a clever prison reference. Prison bars, barbed wire, a shovel, a prison shank, a spoon used to dig a tunnel, a rock pick, a pick-axe, etc.
• 3. Label must tie in apples / apple trees, etc. Something showing what our cider is made of.
• 4. Label must have a memorable font or a logo for brand recognition that will be congruent across all labels.
Should not have
• NO worms in apples please. People do not want to associate or visualize anything like that for food /beverage products.

```html
<!DOCTYPE html>
<html lang="en">
<head>
<meta charset="utf-8">
<title>Tidewhistle Off-Dry Cider Label</title>
<link href="https://fonts.googleapis.com/css2?family=Amatic+SC:wght@700&display=swap" rel="stylesheet">
<style>
  :root {
    --backdrop: #e6eef0;
    --label-paper: #fbf8f2;
    --ink: #111111;
    --cider-red: #e8213f;
    --tally-grey: #c9cac6;
    --tally-grey-soft: #e4e4e0;
    --white: #ffffff;
  }
  * { box-sizing: border-box; margin: 0; padding: 0; }
  html, body {
    width: 840px;
    height: 1200px;
    overflow: hidden;
    background: var(--backdrop);
  }
  .canvas {
    position: relative;
    width: 840px;
    height: 1200px;
  }
  .front-label {
    position: absolute;
    left: 60px;
    top: 185px;
    width: 720px;
    height: 830px;
    background: var(--label-paper);
    border-top: 10px solid var(--ink);
    border-bottom: 10px solid var(--ink);
    font-family: "Amatic SC", "Arial Narrow", sans-serif;
    font-weight: 700;
    color: var(--ink);
  }
  .tally-field {
    position: absolute;
    left: 50px;
    top: 30px;
    width: 620px;
    height: 300px;
    background: linear-gradient(180deg, var(--tally-grey) 0%, var(--tally-grey-soft) 100%);
    opacity: 0.7;
  }
  .brand-seal {
    position: absolute;
    left: 50%;
    top: 60px;
    transform: translateX(-50%);
    width: 190px;
    height: 190px;
    border-radius: 50%;
    background: var(--cider-red);
  }
  .brand-seal-name {
    position: absolute;
    left: 0;
    right: 0;
    top: 262px;
    text-align: center;
    font-size: 40px;
    letter-spacing: 3px;
    color: var(--cider-red);
  }
  .name-banner {
    position: absolute;
    left: 80px;
    top: 340px;
    width: 560px;
    height: 200px;
  }
  .name-banner text {
    font-family: "Amatic SC", "Arial Narrow", sans-serif;
    font-weight: 700;
    font-size: 78px;
    letter-spacing: 4px;
    fill: var(--white);
  }
  .cider-style {
    position: absolute;
    left: 0;
    right: 0;
    top: 540px;
    text-align: center;
    font-size: 52px;
    letter-spacing: 4px;
  }
  .cider-style .star {
    display: inline-block;
    width: 34px;
    height: 34px;
    margin: 0 14px;
    vertical-align: middle;
  }
  .cider-type {
    position: absolute;
    left: 0;
    right: 0;
    top: 620px;
    text-align: center;
    font-size: 58px;
    letter-spacing: 2px;
    color: var(--cider-red);
  }
  .abv-box {
    position: absolute;
    left: 50%;
    top: 715px;
    transform: translateX(-50%);
    padding: 4px 18px;
    background: var(--ink);
    color: var(--white);
    font-size: 36px;
    letter-spacing: 2px;
    border: 3px solid var(--label-paper);
    outline: 2px solid var(--ink);
    white-space: nowrap;
  }
</style>
</head>
<body>
<main class="canvas">
  <section class="front-label">
    <div class="tally-field" role="img" aria-label="Hand-drawn prison tally-mark pattern in grey"></div>
    <div class="brand-seal"></div>
    <div class="brand-seal-name">Tidewhistle</div>

    <svg class="name-banner" viewBox="0 0 560 200" aria-label="Tidewhistle">
      <path d="M10 95 Q280 5 550 95 L520 180 Q280 110 40 180 Z" fill="var(--ink)"/>
      <path id="banner-arc" d="M50 168 Q280 88 510 168" fill="none"/>
      <text text-anchor="middle"><textPath href="#banner-arc" startOffset="50%">TIDEWHISTLE</textPath></text>
    </svg>

    <p class="cider-style">OFF<svg class="star" viewBox="0 0 24 24"><polygon points="12,2 14.9,9 22.5,9.3 16.6,14 18.7,21.5 12,17.2 5.3,21.5 7.4,14 1.5,9.3 9.1,9" fill="none" stroke="var(--ink)" stroke-width="2"/></svg>DRY</p>
    <p class="cider-type">CALIFORNIA HARD APPLE CIDER</p>
    <p class="abv-box">ALC / VOL 7.0%</p>
  </section>
</main>
</body>
</html>
```